Web design for business website

I need a web design for a business website for one of our clients who is specialized in alarm management software. I would like you to design 3 web pages, one for each of the 3 pages. You need to process the corporate identity of our client to the web design. This means the colors of the logo (red and black) should definitely show up on all of the 3 pages. Find the logo file for the logo of our customer. To increase readability I suggest you use a white/light background. All suggestions are welcome.

Please kindly download atttached Webdesign.zip and read the project brief first. The project brief refers to all other files of the zip file. Your design must have exactly the same structure as the wireframes.
Updates

Target Market(s)

B2B, Alarm management

Industry/Entity Type

Business

Number of Pages Required

3 page

Requirements
Must have
• The web design must have exactly the same structure as the wireframes and needs to contain the colors of the company logo.

```html
<!DOCTYPE html>
<html lang="en">
<head>
<meta charset="utf-8">
<title>Kaltris — Alarm insight for operators</title>
<link rel="stylesheet" href="https://fonts.googleapis.com/css2?family=Open+Sans:wght@400;600;700&display=swap">
<style>
:root{
  --brand:#e2461a;
  --ink:#1d1b3a;
  --text:#222;
  --line:#d6d6d6;
  --page:#efefef;
  --white:#fff;
}
*{box-sizing:border-box;margin:0;padding:0}
html,body{width:1136px;height:1200px;overflow:hidden}
body{background:var(--page);font-family:"Open Sans",sans-serif;color:var(--text);position:relative}
.abs{position:absolute}
.topbar{left:0;top:0;width:1136px;height:34px;background:var(--white);border-bottom:1px solid var(--line)}
.topbar .phone{left:103px;top:9px;font-size:13px}
.topbar .phone b{color:var(--brand)}
.lang{left:792px;top:9px;font-size:12px;display:flex;align-items:center;gap:5px}
.flag{width:15px;height:10px;background:#2a3f8f;border:1px solid #b00}
.search{left:865px;top:6px;width:166px;height:22px;border:1px solid #bbb;font-size:12px;color:#888;padding:3px 9px}
.search svg{position:absolute;right:7px;top:4px}
.brand{left:103px;top:54px}
.brand .name{font-weight:700;font-size:40px;color:var(--ink);line-height:1}
.brand .tag{font-size:14px;color:var(--ink);margin-top:6px}
.acct{top:57px;width:64px;height:51px;background:var(--white);border:1px solid var(--line);box-shadow:0 2px 2px rgba(0,0,0,.12);text-align:center;font-size:12px;padding-top:7px}
.acct svg{display:block;margin:0 auto 3px}
.nav{left:103px;top:130px;width:928px;height:42px;background:linear-gradient(#e9501d,#d9400f);display:flex}
.nav a{color:#fff;font-weight:700;font-size:14px;text-decoration:none;padding:0 19px;line-height:42px;border-right:1px solid rgba(0,0,0,.15)}
.nav a.on{background:var(--ink)}
.hero{left:103px;top:177px;width:928px;height:345px;background:linear-gradient(#c9c3ba 0%,#e8c96a 40%,#8f8a52 62%,#4f5233 100%)}
.arrow{width:39px;height:35px;background:var(--white);display:flex;align-items:center;justify-content:center}
.caption{left:201px;top:383px;padding:8px 18px;background:rgba(20,20,20,.75);color:#fff;font-size:15px}
.drop{left:182px;top:172px;width:515px;height:204px;background:var(--white);box-shadow:0 2px 6px rgba(0,0,0,.2)}
.drop .pic{left:19px;top:17px;width:273px;height:123px;background:linear-gradient(#1c3357,#b8902e 60%,#3f5c62)}
.drop .menu{left:300px;top:17px;width:199px}
.drop .menu div{background:#e8e8e8;height:27px;margin-bottom:5px;padding:3px 13px;font-size:14px;color:#333}
.drop .desc{left:21px;top:148px;font-size:12px;line-height:21px;color:#333}
.drop .desc b{font-weight:600;color:#222}
h2{font-size:25px;font-weight:600;text-align:center}
.welcome{left:103px;top:538px;width:928px}
.welcome p{font-size:12.6px;line-height:21.8px;text-align:center;margin-top:12px}
.welcome p+p{margin-top:22px}
.welcome a{color:var(--brand);font-weight:600;text-decoration:none}
.clients-h{left:103px;top:756px;width:928px}
.cnav{top:773px;width:27px;height:22px;border:1px solid var(--line);background:var(--white);display:flex;align-items:center;justify-content:center}
.cnav.next{background:var(--brand);border-color:var(--brand)}
.cards{left:103px;top:806px;display:flex;gap:15.6px}
.card{width:142px;height:89px;background:var(--white);box-shadow:0 1px 3px rgba(0,0,0,.2);display:flex;align-items:center;justify-content:center;font-weight:600;font-size:16px;color:var(--ink)}
.news{left:0;top:926px;width:1136px;height:46px;background:var(--white);border-top:1px solid var(--line);border-bottom:1px solid var(--line)}
.social{left:104px;top:13px;display:flex;gap:11px}
.social span{width:23px;height:23px;border:1.5px solid #444;border-radius:50%}
.news .label{left:650px;top:11px;font-size:15px}
.news .field{left:733px;top:9px;width:202px;height:27px;border:1px solid #ccc;font-size:12.5px;color:#555;padding:4px 9px}
.news .btn{left:941px;top:9px;width:89px;height:27px;background:var(--brand);color:#fff;font-size:14px;text-align:center;line-height:27px}
.footer{left:0;top:972px;width:1136px;height:178px;background:var(--white)}
.col{top:12px}
.col h3{font-size:14.5px;font-weight:600;color:#333;margin-bottom:8px}
.col li{list-style:none;font-size:13px;color:#444;line-height:26.4px}
.contact li{display:flex;gap:14px;line-height:19px;margin-bottom:10px;font-size:12.6px}
.contact svg{flex:none;margin-top:2px}
.copy{left:0;top:1150px;width:1136px;height:50px;border-top:1px solid var(--line);text-align:center;font-size:11.5px;color:#444;line-height:48px}
</style>
</head>
<body>
<div class="abs topbar">
  <div class="abs phone"><b>T</b> +31 (0)20 555 0142</div>
  <div class="abs lang"><span class="flag"></span>ENG ▾</div>
  <div class="abs search">Search<svg width="12" height="12" viewBox="0 0 12 12"><circle cx="5" cy="5" r="4" fill="none" stroke="#999" stroke-width="1.4"/><path d="M8 8l3 3" stroke="#999" stroke-width="1.4"/></svg></div>
</div>

<div class="abs brand">
  <div class="name">Kaltris</div>
  <div class="tag">Alarm insight for operators</div>
</div>
<div class="abs acct" style="left:812px"><svg width="16" height="18" viewBox="0 0 16 18"><circle cx="8" cy="5" r="4" fill="#777"/><path d="M1 18c0-6 14-6 14 0z" fill="#777"/></svg>Account</div>
<div class="abs acct" style="left:887px"><svg width="14" height="18" viewBox="0 0 14 18"><path d="M3 8V5a4 4 0 018 0v3" fill="none" stroke="#777" stroke-width="2"/><rect x="1" y="8" width="12" height="10" fill="#777"/></svg>Log in</div>
<div class="abs acct" style="left:963px"><svg width="18" height="18" viewBox="0 0 18 18"><circle cx="7" cy="5" r="4" fill="#777"/><path d="M0 18c0-6 14-6 14 0z" fill="#777"/><circle cx="14" cy="13" r="3.5" fill="#fff" stroke="#777"/></svg>Sign up</div>

<nav class="abs nav">
  <a class="on">HOME</a><a>INDUSTRY</a><a>TELECOM</a><a>POWER</a><a>UTILITIES</a><a style="border:0">INFRA STORE</a>
</nav>

<div class="abs hero" role="img" aria-label="Industrial plant skyline at sunset behind a marshy pond"></div>
<div class="abs arrow" style="left:127px;top:333px"><svg width="10" height="14" viewBox="0 0 10 14"><path d="M8 1L2 7l6 6" fill="none" stroke="#222" stroke-width="1.6"/></svg></div>
<div class="abs arrow" style="left:972px;top:333px"><svg width="10" height="14" viewBox="0 0 10 14"><path d="M2 1l6 6-6 6" fill="none" stroke="#222" stroke-width="1.6"/></svg></div>
<div class="abs caption">Lorem Ipsum is simply dummy text of the printing</div>

<div class="abs drop">
  <div class="abs pic" role="img" aria-label="Refinery lit up at dusk"></div>
  <div class="abs menu"><div>Alarm Management</div><div>Asset Management</div><div>Predictive Maintenance</div><div>Logic Design</div></div>
  <div class="abs desc">Lorem Ipsum is simply dummy text of the printing and typesetting industry.<br>Lorem Ipsum has been the industry's standard &nbsp; <b>View Detail ›</b></div>
</div>

<section class="abs welcome">
  <h2>Welcome Kaltris</h2>
  <p>Lorem Ipsum is simply dummy text of the printing and typesetting industry. Lorem Ipsum has been the industry's standard dummy text ever since the 1500s, when an unknown printer took a galley of type and scrambled it to make a type specimen book. It has survived not only five centuries, but also the leap into electronic typesetting, remaining essentially unchanged. It was popularised in the 1960s with the release of Typeset sheets containing Lorem Ipsum passages, and more recently with desktop publishing software like Pagecraft Studio including versions of Lorem Ipsum.</p>
  <p>Contrary to popular belief, Lorem Ipsum is not simply random text. It has roots in a piece of classical Latin literature from 45 BC, making it over 2000 years old. Edwin Harrowgate, a Latin professor at Brookmere College in Virginia, looked up one of the more obscure Latin words, consectetur <a>Know More</a></p>
</section>

<h2 class="abs clients-h">Our clients</h2>
<div class="abs cnav" style="left:970px"><svg width="7" height="11" viewBox="0 0 7 11"><path d="M6 1L1.5 5.5 6 10" fill="none" stroke="#222" stroke-width="1.4"/></svg></div>
<div class="abs cnav next" style="left:1004px"><svg width="7" height="11" viewBox="0 0 7 11"><path d="M1 1l4.5 4.5L1 10" fill="none" stroke="#fff" stroke-width="1.4"/></svg></div>
<div class="abs cards">
  <div class="card">Corvane</div>
  <div class="card">Meridal</div>
  <div class="card">Nordhaven</div>
  <div class="card">Tessaline</div>
  <div class="card">Brouwvik</div>
  <div class="card">Ostrel</div>
</div>

<div class="abs news">
  <div class="abs social"><span aria-label="Social page one"></span><span aria-label="Social page two"></span><span aria-label="Social page three"></span></div>
  <div class="abs label">Newsletter</div>
  <div class="abs field">Enter you email address</div>
  <div class="abs btn">Subscribe</div>
</div>

<footer class="abs footer">
  <div class="abs col" style="left:103px"><h3>Solutions</h3><ul><li>Alarm Reporting Suite</li><li>Alarm Analysis Suite</li><li>Alarm Advisor Suite</li><li>Consulting</li></ul></div>
  <div class="abs col" style="left:311px"><h3>Industries</h3><ul><li>Industry</li><li>Telecom</li><li>Power</li><li>Utilities</li><li>Infra</li></ul></div>
  <div class="abs col" style="left:461px"><h3>About us</h3><ul><li>Company</li><li>Overview</li><li>Leadership</li><li>Partners</li><li>Locations</li></ul></div>
  <div class="abs col" style="left:600px"><h3>News</h3><ul><li>Product News</li><li>Partner News</li><li>Events</li><li>Press Releases</li><li>Vacancies</li></ul></div>
  <div class="abs col contact" style="left:764px"><h3>Contact details</h3><ul>
    <li><svg width="16" height="20" viewBox="0 0 16 20"><path d="M8 0a7 7 0 00-7 7c0 5 7 13 7 13s7-8 7-13a7 7 0 00-7-7z" fill="#888"/><circle cx="8" cy="7" r="2.5" fill="#fff"/></svg><span>Kaltris, 18 Larkfield Lane<br>Ashford, AF 210, USA</span></li>
    <li><svg width="16" height="18" viewBox="0 0 16 18"><rect x="3" y="1" width="10" height="16" rx="2" fill="#888"/><rect x="5" y="4" width="6" height="4" fill="#fff"/></svg><span>Call us now toll free: +001 555 017<br>+001 555 042, +11 555 0190</span></li>
    <li><svg width="16" height="12" viewBox="0 0 16 12"><rect width="16" height="12" fill="#888"/><path d="M0 0l8 7 8-7" fill="none" stroke="#fff" stroke-width="1.3"/></svg><span>Customer support: help@kaltris.test<br>Live chat: 9:00–17:00</span></li>
  </ul></div>
</footer>
<div class="abs copy">Copyright © 2015 Kaltris. All Rights Reserved.</div>
</body>
</html>
```